Newsletter Design Project

Hi there! I am an sketch artist/educator in the wedding space and need a few newsletter templates that someone on my team can easily drop in text and photos, but look clean, high end, and that can represent my brand well.
Updates

Reason: We have edits out to a designer and waiting for the design to come back.

Target Market(s)

High end - luxury (but approachable) wedding planners

Industry/Entity Type

Wedding

Font styles to use
Serif

Colors

Designer to choose colors to be used in the design.

Requirements
Must have
• Easy templates that can be dropped into mailchimp and where we can drop in text/photos very easily. Clean layout design. I think I'm looking for something white and gray - since all my images will have the color. But will leave it up to the designers.
Should not have
• nothing over the top or fancy.

```html
<!DOCTYPE html>
<html lang="en">
<head>
<meta charset="utf-8">
<title>Petal Lane Studio Newsletter</title>
<link rel="stylesheet" href="https://fonts.googleapis.com/css2?family=Lato:ital,wght@0,300;0,400;0,700;1,300;1,400&family=Libre+Baskerville:ital@0;1&display=swap">
<style>
:root{
  --white:#ffffff;
  --ink:#2b2b2b;
  --text:#555555;
  --muted:#7a7a7a;
  --rose:#e3a79c;
  --rose-btn:#d9a5a0;
  --rose-deep:#dca4a5;
  --peach-light:#fbe3da;
  --peach:#f7b8a8;
  --coral:#f5a690;
  --blush:#f3e1e0;
  --gray-band:#ececec;
  --link:#3b8fc4;
}
*{margin:0;padding:0;box-sizing:border-box}
html,body{width:1200px;height:3301px;overflow:hidden;background:var(--white)}
body{position:relative;font-family:'Lato',sans-serif;color:var(--text)}
.abs{position:absolute}

/* header */
.brand{font-family:'Lato',sans-serif;font-weight:400;color:var(--ink);letter-spacing:4px;text-transform:uppercase;line-height:1.25}
.brand-left{left:100px;top:64px;font-size:30px;color:var(--rose)}
.brand-right{right:70px;top:80px;font-size:30px;text-align:right}

/* hero */
.hero{left:21px;top:217px;width:1158px;height:515px;
  background:radial-gradient(ellipse at 30% 70%,#f2b8a6 0%,rgba(242,184,166,0) 45%),
             radial-gradient(ellipse at 80% 75%,#f3a99a 0%,rgba(243,169,154,0) 40%),
             radial-gradient(ellipse at 60% 20%,#d9d06a 0%,rgba(217,208,106,0) 35%),
             linear-gradient(180deg,#5d7a45 0%,#7b8a5a 45%,#b99a86 100%)}
.hero-shade{left:21px;top:217px;width:1158px;height:515px;background:rgba(40,40,40,.28)}
.hero-title{left:21px;top:288px;width:1158px;text-align:center;font-family:'Libre Baskerville',serif;font-size:56px;color:var(--white)}
.hero-copy{left:180px;top:396px;width:840px;font-family:'Libre Baskerville',serif;font-style:italic;font-size:22px;line-height:35px;color:var(--white)}
.btn-solid{display:flex;align-items:center;justify-content:center;background:var(--rose-btn);color:var(--white);font-weight:700;letter-spacing:5px;text-transform:uppercase}
.hero-btn{left:457px;top:582px;width:286px;height:58px;font-size:22px}

/* shared section type */
.section-title{left:0;width:1200px;text-align:center;font-weight:300;letter-spacing:1px;text-transform:uppercase}
.title-rose{font-size:54px;color:var(--rose)}
.title-ink{font-size:44px;color:var(--ink);font-weight:400}
.body-copy{left:48px;width:1115px;text-align:center;font-size:28px;line-height:61px;color:var(--text)}
.btn-outline{display:flex;align-items:center;justify-content:center;border:3px solid var(--rose);color:var(--rose);font-size:28px;font-weight:300;letter-spacing:3px;text-transform:uppercase}

.welcome-title{top:762px}
.welcome-copy{top:844px}
.quote{left:80px;width:1060px;top:1110px;font-style:italic;font-weight:300;font-size:37px;line-height:58px;color:var(--text)}
.btn-learn-1{left:463px;top:1285px;width:267px;height:66px}

/* announcements */
.announce-bg{left:0;top:1427px;width:1200px;height:410px;
  background:radial-gradient(ellipse at 8% 30%,#f9ddd3 0%,rgba(249,221,211,0) 30%),
             radial-gradient(ellipse at 55% 10%,#fbe4dc 0%,rgba(251,228,220,0) 30%),
             radial-gradient(ellipse at 92% 40%,#f9dbd0 0%,rgba(249,219,208,0) 30%),
             linear-gradient(180deg,#fdf3ef,#fff8f5)}
.announce-title{top:1444px}
.card-img{width:283px;height:243px;box-shadow:0 2px 6px rgba(0,0,0,.18)}
.card-img-1{left:21px;top:1546px;background:linear-gradient(135deg,#c79a5a 0%,#f4efe6 40%,#f3e7d6 70%,#2f7a6f 100%)}
.card-img-2{left:608px;top:1546px;background:linear-gradient(180deg,#f2b3a3 0%,#e85a54 45%,#f6d3c8 70%,#e4473f 100%)}
.card-text{width:265px;font-size:17px;line-height:29px;color:var(--text)}
.card-text h3{font-size:17px;font-weight:700;color:var(--ink);line-height:29px}
.card-text .more{color:var(--rose)}
.card-text-1{left:323px;top:1540px}
.card-text-2{left:915px;top:1540px}

/* summer sessions */
.sessions-band{left:0;top:1837px;width:1200px;height:259px;background:var(--gray-band)}
.sessions-title{left:37px;top:1882px;font-size:42px;font-weight:700;letter-spacing:4px;color:var(--ink);text-transform:uppercase}
.sessions-rule{left:37px;top:1976px;width:95px;height:3px;background:var(--rose)}
.sessions-list{left:153px;top:1963px;width:700px;font-size:16px;font-weight:700;letter-spacing:1.5px;line-height:45px;color:var(--ink);text-transform:uppercase}
.contact-btn{left:883px;top:1940px;width:285px;height:61px;font-size:27px;letter-spacing:3px}

/* mission */
.mission-title{top:2150px}
.mission-copy{top:2236px;line-height:57px}
.btn-learn-2{left:463px;top:2561px;width:267px;height:66px}

/* offer */
.offer-title{top:2720px}
.offer-tile{display:flex;align-items:center;justify-content:center;font-size:30px;letter-spacing:10px;text-transform:uppercase;color:var(--white)}
.tile-courses{left:66px;top:2804px;width:518px;height:59px;background:var(--peach-light);color:#c9a9a0}
.tile-stories{left:592px;top:2804px;width:521px;height:59px;background:var(--peach)}
.tile-products{left:66px;top:2870px;width:1047px;height:58px;background:var(--coral)}
.tile-ecourses{left:66px;top:2934px;width:518px;height:58px;background:var(--rose-deep)}
.tile-design{left:592px;top:2934px;width:521px;height:58px;background:var(--blush);color:#d8c2c0}

/* contact bar */
.contact-bar{left:0;top:3040px;width:1200px;height:87px;background:var(--gray-band)}
.need-help{left:98px;top:3068px;font-size:24px;font-weight:700;color:var(--rose);text-transform:uppercase}
.mail-icon{left:348px;top:3069px}
.mail-addr{left:398px;top:3067px;font-size:25px;font-weight:700;color:var(--ink)}
.social{top:3068px;width:32px;height:32px;border-radius:3px}
.social-1{left:905px;background:#3b5998}
.social-2{left:965px;background:#b5835a}
.social-3{left:1025px;background:#cb2027}
.social-4{left:1085px;background:#1da1f2}

/* footer */
.footer{left:0;top:3127px;width:1200px;height:174px;
  background:radial-gradient(ellipse at 20% 40%,#fbe7e0 0%,rgba(251,231,224,0) 40%),
             radial-gradient(ellipse at 75% 60%,#fbe4dc 0%,rgba(251,228,220,0) 40%),#fff8f6}
.footer-text{left:34px;top:3184px;font-size:17px;line-height:35px;color:var(--muted)}
.footer-text a{color:var(--link);text-decoration:none}
.footer-text .u{text-decoration:underline}
.footer-text .pink{color:var(--rose);text-transform:uppercase}
.footer-brand{right:70px;top:3205px;font-size:28px}
</style>
</head>
<body>

<header>
  <div class="abs brand brand-left">Petal Lane<br>Studio</div>
  <div class="abs brand brand-right">The Drawing Room<br>Series</div>
</header>

<section class="hero-section">
  <div class="abs hero" role="img" aria-label="Photo of a lush floral arrangement with pink blooms and green foliage"></div>
  <div class="abs hero-shade"></div>
  <h1 class="abs hero-title" style="font-weight:400">Live a Creatively Inspired Life</h1>
  <p class="abs hero-copy">A custom artwork is an agreement between the artist and a private party. You to create artwork based on your requests. Typically people ask for custom work of their wedding design, events, heirlooms, gifts, interiors, restaurants, custom.</p>
  <a class="abs btn-solid hero-btn">Shop Now</a>
</section>

<section class="welcome">
  <h2 class="abs section-title title-rose welcome-title">Welcome</h2>
  <p class="abs body-copy welcome-copy">Hi! I’m Clara Wren – founder and creator of Petal Lane Studio &amp; The Drawing Room Series. I’ve always known that I wanted to live a creatively inspired life. At an early age, I would sit and sketch for hours, focusing on the smallest details. My passion is connecting and inspiring other creatives through art + design (cont.)</p>
  <blockquote class="abs quote">“I find that a beautiful sketch is the entry point to every great idea + that creativity is our form of community.”</blockquote>
  <a class="abs btn-outline btn-learn-1">Learn More</a>
</section>

<section class="announcements">
  <div class="abs announce-bg" role="img" aria-label="Soft blush watercolor wash background"></div>
  <h2 class="abs section-title title-ink announce-title">Announcements</h2>
  <div class="abs card-img card-img-1" role="img" aria-label="Photo of a sketchbook, pencils and a gold pineapple on a desk"></div>
  <div class="abs card-text card-text-1">
    <h3>GATHER 2016! - Grand Finale</h3>
    <p>I Hard to believe that our Mexico sketch class was just last month, but wanted to share some of the amazing details from this class! inspired by this amazing setting and location?</p>
    <p class="more">Read More</p>
  </div>
  <div class="abs card-img card-img-2" role="img" aria-label="Photo of illustrated pineapple cards on a red striped table"></div>
  <div class="abs card-text card-text-2">
    <h3>GATHER 2016! - Grand Finale</h3>
    <p>I Hard to believe that our Mexico sketch class was just last month, but wanted to share some of the amazing details from this class! inspired by this amazing setting and location?</p>
    <p class="more">Read More</p>
  </div>
</section>

<section class="sessions">
  <div class="abs sessions-band"></div>
  <h2 class="abs sessions-title">Design Summer Sessions</h2>
  <div class="abs sessions-rule"></div>
  <p class="abs sessions-list">Floral Sketching, Sketch Cakes &amp; Desserts, Water Color Technic<br>Fashion Illustrations</p>
  <a class="abs btn-solid contact-btn">Contact Us</a>
</section>

<section class="mission">
  <h2 class="abs section-title title-rose mission-title">Our Mission</h2>
  <p class="abs body-copy mission-copy">Our mission is to encourage as many creatives to dream of a life they’ve always wanted. We are a team of passionate artists, designers, creators, and go-getters who share a common goal of making an impact through our work.&nbsp; We are here to serve the creative community through education, connection, inspiration, and sharing in thoughtful conversations.&nbsp; We hope our work inspires you to take action.</p>
  <a class="abs btn-outline btn-learn-2">Learn More</a>
</section>

<section class="offer">
  <h2 class="abs section-title title-ink offer-title">What We Offer</h2>
  <a class="abs offer-tile tile-courses">Courses</a>
  <a class="abs offer-tile tile-stories">Inspiration Stories</a>
  <a class="abs offer-tile tile-products">Products</a>
  <a class="abs offer-tile tile-ecourses">E-Courses</a>
  <a class="abs offer-tile tile-design">Design Inspiration</a>
</section>

<section class="contact">
  <div class="abs contact-bar"></div>
  <p class="abs need-help">Need Help</p>
  <svg class="abs mail-icon" width="38" height="28" viewBox="0 0 38 28" aria-hidden="true">
    <rect x="1.5" y="1.5" width="35" height="25" fill="none" stroke="#2b2b2b" stroke-width="3"/>
    <path d="M2 3 L19 16 L36 3" fill="none" stroke="#2b2b2b" stroke-width="3"/>
  </svg>
  <p class="abs mail-addr">hello@petallanestudio.com</p>
  <span class="abs social social-1" aria-label="Social link"></span>
  <span class="abs social social-2" aria-label="Social link"></span>
  <span class="abs social social-3" aria-label="Social link"></span>
  <span class="abs social social-4" aria-label="Social link"></span>
</section>

<footer>
  <div class="abs footer"></div>
  <p class="abs footer-text">We are sending you this email because you subscribed to our newsletter.<br>We’ll be sad to see you go, but <a>you can always</a> <a class="u">Unsubscribe from emails</a><br><span class="pink">2017 Petal Lane Studio &nbsp; | &nbsp; Privacy Policy + Terms</span></p>
  <div class="abs brand footer-brand">The Drawing Room<br>Series</div>
</footer>

</body>
</html>
```